JMT - Business Card Design Project

We need a business card based on our logo
Updates

Hi I just upload logo file in AI format Thanks and regards

Target Market(s)

Bank, Big companies, Business owners

Industry/Entity Type

Business

Font styles to use
Sans Serif

```html
<!DOCTYPE html>
<html lang="en">
<head>
<meta charset="utf-8">
<title>JMT – Business Card</title>
<link rel="stylesheet" href="https://fonts.googleapis.com/css2?family=Didact+Gothic&family=Open+Sans:wght@400;600&display=swap">
<style>
  :root {
    --backdrop: #e9e9ec;
    --card-white: #ffffff;
    --navy: #0f1c3c;
    --slate: #8a9599;
    --slate-light: #a3adb1;
    --text-light: #ffffff;
    --divider: #6c7690;
  }
  * { box-sizing: border-box; margin: 0; padding: 0; }
  html, body {
    width: 1200px; height: 800px; overflow: hidden;
    background: var(--backdrop);
  }
  .stage { position: relative; width: 1200px; height: 800px; }
  .card {
    position: absolute; left: 150px; top: 143px;
    width: 900px; height: 514px;
    background: var(--card-white);
    overflow: hidden;
    box-shadow: 0 6px 24px rgba(0,0,0,0.18);
  }
  .card-shapes { position: absolute; inset: 0; width: 900px; height: 514px; }
  .shape-navy { fill: var(--navy); }
  .shape-accent { fill: var(--slate); }

  .brand { position: absolute; left: 62px; top: 92px; color: var(--navy); font-family: "Didact Gothic", sans-serif; }
  .brand-mark { font-size: 132px; line-height: 1; letter-spacing: 2px; }
  .brand-name { font-size: 31px; line-height: 1.1; margin-top: 2px; }
  .brand-tagline {
    font-family: "Didact Gothic", sans-serif; color: var(--slate);
    font-size: 13.5px; letter-spacing: 0.4px; margin-top: 4px;
  }

  .holder {
    position: absolute; right: 344px; top: 318px; text-align: right;
    font-family: "Open Sans", sans-serif;
  }
  .holder-name { color: var(--slate-light); font-size: 29px; font-weight: 600; line-height: 1.15; }
  .holder-role { color: var(--text-light); font-size: 17px; line-height: 1.3; }

  .divider {
    position: absolute; left: 590px; top: 250px; width: 1px; height: 160px;
    background: var(--divider);
  }

  .contacts {
    position: absolute; left: 606px; top: 238px; list-style: none;
    font-family: "Open Sans", sans-serif; color: var(--text-light);
    font-size: 19px; line-height: 29px;
  }
  .contacts li { display: flex; align-items: flex-start; }
  .contact-icon { width: 20px; height: 20px; margin: 5px 8px 0 0; flex: none; fill: var(--text-light); }
  .contact-text { display: block; }
</style>
</head>
<body>
<main class="stage">
  <section class="card" aria-label="JMT business card">
    <svg class="card-shapes" viewBox="0 0 900 514" aria-hidden="true">
      <path class="shape-accent" d="M560 214 C720 150 818 72 846 0 L880 0 C848 92 740 172 560 214 Z"/>
      <path class="shape-navy" d="M40 514 C120 380 360 330 560 240 C720 170 830 90 872 0 L900 0 L900 514 Z"/>
    </svg>

    <div class="brand">
      <div class="brand-mark">JMT</div>
      <div class="brand-name">Cabinet Jourdan &amp; Associés</div>
      <div class="brand-tagline">Expertise-comptable · Audit · Conseil</div>
    </div>

    <div class="holder">
      <p class="holder-name">Marc Delorme</p>
      <p class="holder-role">Manager</p>
    </div>

    <div class="divider"></div>

    <ul class="contacts">
      <li>
        <svg class="contact-icon" viewBox="0 0 20 20" aria-hidden="true"><path d="M6 1h8a1.5 1.5 0 0 1 1.5 1.5v15A1.5 1.5 0 0 1 14 19H6a1.5 1.5 0 0 1-1.5-1.5v-15A1.5 1.5 0 0 1 6 1zm0 2.5v11h8v-11zm4 12a1 1 0 1 0 0 2 1 1 0 0 0 0-2z"/></svg>
        <span class="contact-text">154 555 0192</span>
      </li>
      <li>
        <svg class="contact-icon" viewBox="0 0 20 20" aria-hidden="true"><path d="M4.5 2l3 3.2-1.6 2.2c1 2.2 2.6 3.8 4.8 4.8l2.2-1.6 3.1 3-1.8 3.2C8.6 16.4 3.6 11.4 1.3 5z"/></svg>
        <span class="contact-text">154 555 0147</span>
      </li>
      <li>
        <svg class="contact-icon" viewBox="0 0 20 20" aria-hidden="true"><path d="M10 1a9 9 0 1 0 0 18 9 9 0 0 0 0-18zm6.9 8h-3.1a14 14 0 0 0-1.2-5.6A7 7 0 0 1 16.9 9zM10 3c.9 1.2 1.7 3.4 1.8 6H8.2C8.3 6.4 9.1 4.2 10 3zM7.4 3.4A14 14 0 0 0 6.2 9H3.1a7 7 0 0 1 4.3-5.6zM3.1 11h3.1a14 14 0 0 0 1.2 5.6A7 7 0 0 1 3.1 11zm6.9 6c-.9-1.2-1.7-3.4-1.8-6h3.6c-.1 2.6-.9 4.8-1.8 6zm2.6-.4a14 14 0 0 0 1.2-5.6h3.1a7 7 0 0 1-4.3 5.6z"/></svg>
        <span class="contact-text">www.jmtcabinet.com</span>
      </li>
      <li>
        <svg class="contact-icon" viewBox="0 0 20 20" aria-hidden="true"><path d="M2 4h16v12H2zm1.8 1.5L10 10.3l6.2-4.8zM3.5 7.3v7.2h13V7.3L10 12.2z"/></svg>
        <span class="contact-text">info@jmtcabinet.com</span>
      </li>
      <li>
        <svg class="contact-icon" viewBox="0 0 20 20" aria-hidden="true"><path d="M10 2l9 8h-2.5v8h-5v-5h-3v5h-5v-8H1z"/></svg>
        <span class="contact-text">Po Box: 418 Linden Rd.<br>Fairview, NJ. 07022</span>
      </li>
    </ul>
  </section>
</main>
</body>
</html>
```